7QK Pop Up Shop Clearance Flyer

We sell furniture. We opened up recently a temporary pop up shop to clear some stock we had from our old shop. So we don't have a full collection just our clearance lines that we want to get rid of - but the customer doesn't need to know this! Therefore the aim of this leaflet is to attract customers and make them come in - once they are there they might see something they like. As we will not be there for long - just a few more weeks.
We need a flyer to promote locally our pop up shop (temporary shop) with a Clearance Sale. The flyer will be sent by post or by hand to the local residents and by email to ex customers that bought from us before and we have their email address...
We need a modern fresh design flyer. At the next stage we will provide text for each item (brief description, dimensions and price) so allow some space for this.
Maybe we need to add a message or something to make people want to come quickly? For example most of the items are ex display or the last item and if they want it they should hurry as one is gone its gone. or you may have a better suggestion - let me know.
if you want to see some ideas of our website then 7QK.co.uk

Target Market(s)

Local Residents around shop

Industry/Entity Type

Retail

Colors
0255a3
3176b5
85abd2

Requirements
Must have
• price tag showing RRP or WAS price and the Clearance Sale price
• Opening Hours: Mon-Fri 9:00am - 5:00pm, Sat: 9:00am - 4:00pm, Sun: Closed
• Tel: 0208 915 2730
• Shop Address: 184 Birch Rowe, Elmwick Vale, London, N21 7PD
Nice to have
• Parking behind Bo Tarvins
• Map of location

```html
<!DOCTYPE html>
<html lang="en">
<head>
<meta charset="utf-8">
<title>7QK Clearance Sale Flyer</title>
<link href="https://fonts.googleapis.com/css2?family=Saira:ital,wght@1,500;1,800&family=Lato:wght@400;700;900&family=Montserrat:wght@700&display=swap" rel="stylesheet">
<style>
  :root{
    --brand-blue:#0255a3;
    --mid-blue:#3176b5;
    --light-blue:#85abd2;
    --deep-blue:#0b3f8c;
    --ink:#1d1d1f;
    --grey:#6b6b6b;
    --rule:#9a9a9a;
    --paper:#ffffff;
    --backdrop:#eceef1;
  }
  *{margin:0;padding:0;box-sizing:border-box;}
  html,body{width:1112px;height:1200px;overflow:hidden;background:var(--backdrop);}
  .flyer{
    position:absolute;left:136px;top:14px;width:800px;height:1115px;
    background:var(--paper);transform:scale(1.05);transform-origin:top left;
    overflow:hidden;font-family:"Lato",sans-serif;
    box-shadow:0 4px 18px rgba(0,0,0,.12);
  }
  .headline{
    position:absolute;left:54px;top:50px;white-space:nowrap;
    font-family:"Saira",sans-serif;font-style:italic;font-weight:800;
    font-size:96px;letter-spacing:-3px;line-height:1;color:var(--brand-blue);
  }
  .subline{
    position:absolute;left:64px;top:166px;white-space:nowrap;
    font-family:"Saira",sans-serif;font-style:italic;font-weight:500;
    font-size:27px;line-height:35px;color:var(--grey);letter-spacing:-.5px;
  }
  .hero-photo{
    position:absolute;left:10px;top:268px;width:580px;height:282px;
    background:linear-gradient(135deg,#eceae6 0%,#d9d6d0 40%,#8a7a68 70%,#c46a55 100%);
  }
  .shapes{position:absolute;left:0;top:0;}
  .hero-price{position:absolute;right:34px;top:268px;text-align:right;color:#fff;}
  .hero-price .now{font-family:"Montserrat",sans-serif;font-weight:700;font-size:72px;line-height:1;}
  .hero-price .amount{font-weight:900;font-size:50px;line-height:1.2;}
  .hero-price .old{font-weight:900;font-size:27px;line-height:33px;margin-top:26px;}
  .item{position:absolute;left:34px;width:342px;}
  .item-photo{height:166px;}
  .item-one{top:612px;}
  .item-two{top:843px;left:28px;}
  .item-one .item-photo{background:linear-gradient(160deg,#f1f0ee 0%,#e2dfda 55%,#a89888 100%);}
  .item-two .item-photo{background:linear-gradient(160deg,#e6d9cf 0%,#c98f3e 55%,#7b5638 100%);}
  .item-price{
    height:35px;background:var(--brand-blue);color:#fff;white-space:nowrap;
    font-weight:900;font-size:15.5px;line-height:35px;text-align:center;
  }
  .hours{
    position:absolute;left:416px;top:740px;width:334px;height:76px;
    border:3px solid var(--brand-blue);text-align:center;color:var(--brand-blue);
    font-weight:900;font-size:18px;line-height:23px;
  }
  .hours-title{
    position:absolute;left:50%;top:-13px;transform:translateX(-50%);
    background:var(--paper);padding:0 6px;white-space:nowrap;
  }
  .hours-list{margin-top:12px;white-space:nowrap;}
  .hours-closed{
    position:absolute;left:50%;bottom:-13px;transform:translateX(-50%);
    background:var(--paper);padding:0 6px;white-space:nowrap;
  }
  .brand{
    position:absolute;left:410px;top:852px;display:flex;align-items:center;gap:12px;
  }
  .brand-mark{width:40px;height:40px;background:var(--ink);}
  .brand-text{display:flex;flex-direction:column;align-items:flex-end;}
  .brand-name{font-weight:400;font-size:25px;line-height:28px;color:var(--ink);letter-spacing:.3px;white-space:nowrap;}
  .brand-tagline{font-weight:400;font-size:12px;line-height:15px;color:var(--ink);white-space:nowrap;}
  .contact{
    position:absolute;left:410px;top:930px;width:342px;height:135px;
    background:var(--mid-blue);color:#fff;text-align:center;padding-top:14px;
  }
  .contact .tel{font-weight:900;font-size:30px;line-height:36px;white-space:nowrap;}
  .contact .divider{width:266px;height:2px;background:#fff;margin:6px auto 7px;}
  .contact .address{font-size:14.5px;line-height:17px;}
</style>
</head>
<body>
  <main class="flyer">
    <h1 class="headline">Clearance Sale</h1>
    <p class="subline">For All Types Of Furnitures Supplied<br>From Basic To Luxury</p>

    <div class="hero-photo" role="img" aria-label="Photo of a bedroom with a dark wood bed, striped bedding, bedside tables with lamps and a terracotta rug"></div>

    <svg class="shapes" width="800" height="1115" viewBox="0 0 800 1115" aria-hidden="true">
      <defs>
        <linearGradient id="bandFade" x1="0" y1="0" x2="1" y2="0">
          <stop offset="0" stop-color="#0b3f8c"/>
          <stop offset="1" stop-color="#0255a3"/>
        </linearGradient>
      </defs>
      <rect x="0" y="252" width="380" height="10" fill="#9a9a9a"/>
      <rect x="0" y="548" width="330" height="8" fill="#9a9a9a"/>
      <polygon points="380,222 412,222 438,268 372,268" fill="#0255a3"/>
      <polygon points="392,222 800,222 800,556 590,556" fill="#1d1d1f"/>
      <rect x="540" y="420" width="226" height="2" fill="#fff"/>
      <polygon points="320,556 610,556 560,634 510,634" fill="#0255a3"/>
      <polygon points="510,634 560,634 536,658" fill="#1d1d1f"/>
      <polygon points="612,556 800,556 800,662 540,662" fill="url(#bandFade)"/>
    </svg>

    <div class="hero-price">
      <div class="now">NOW</div>
      <div class="amount">$ 00.00</div>
      <div class="old">RRP $ 00.00<br>WAS $ 00.00</div>
    </div>

    <section class="item item-one">
      <div class="item-photo" role="img" aria-label="Photo of a grey upholstered chaise lounge in a bright white room"></div>
      <div class="item-price">NOW $ 00.00 | RRP $ 00.00 | WAS $ 00.00</div>
    </section>

    <section class="item item-two">
      <div class="item-photo" role="img" aria-label="Photo of a mustard wingback armchair beside a small white side table"></div>
      <div class="item-price">NOW $ 00.00 | RRP $ 00.00 | WAS $ 00.00</div>
    </section>

    <section class="hours">
      <span class="hours-title">Opening Hours:</span>
      <div class="hours-list">Monday to Friday: 9:00am-5:00pm<br>Saturday : 9:00am-4:00pm</div>
      <span class="hours-closed">Sunday: Closed</span>
    </section>

    <div class="brand">
      <span class="brand-mark"></span>
      <div class="brand-text">
        <span class="brand-name">7QK FURNITURE</span>
        <span class="brand-tagline">TRADE FURNITURE SOLUTIONS</span>
      </div>
    </div>

    <section class="contact">
      <div class="tel">Tel: 0208 915 2730</div>
      <div class="divider"></div>
      <div class="address">Shop Address: 184 Birch Rowe,<br>Elmwick Vale, London, N21 7PD<br>Parking : behind Bo Tarvins</div>
    </section>
  </main>
</body>
</html>
```